hawkiron structural steel

8 1/2" x 11" flyer color both sides. Use at least 12 pictures.

Add the word; structural under HawkIron to logo

bullet points:
Laser Accuracy
On-time scheduling
Own our Equipment
39 Years Exp.
Manufacturing Construction Brackets Since 1982
We manufacture custom ibeams in Phoenix, AZ
Certified welders

Hawkiron Plant
4812 n. 27th street, suite-3
Phx, AZ 85019
480-926-8147

Target Market(s)

Architects, builders

Industry/Entity Type

construction

Colors
0054AA
0677BA
7BADD7
CADEEF
E8F1F8

```html
<!DOCTYPE html>
<html lang="en">
<head>
<meta charset="utf-8">
<title>HawkIron Structural Flyer</title>
<link href="https://fonts.googleapis.com/css2?family=Roboto+Condensed:wght@400&display=swap" rel="stylesheet">
<style>
  :root {
    --navy: #445f8c;
    --steel-blue: #2f86b4;
    --sky: #4aa2cf;
    --address-blue: #3b9cc9;
    --tile-fill: #d9eaf6;
    --icon-ink: #22508f;
    --white: #ffffff;
    --bar-edge: #3a5a9c;
    --bar-mid: #9fb5da;
  }
  * { margin: 0; padding: 0; box-sizing: border-box; }
  html, body { width: 781px; height: 1200px; overflow: hidden; background: var(--white); }
  body { font-family: "Roboto Condensed", "Arial Narrow", sans-serif; color: var(--white); }
  .flyer { position: relative; width: 781px; height: 1200px; overflow: hidden; }

  .masthead { position: absolute; left: 0; top: 0; width: 781px; height: 467px; background: var(--navy); }
  .mark-circle { position: absolute; left: 300px; top: 60px; width: 180px; height: 180px; border-radius: 50%; background: var(--white); opacity: .92; }
  .brand-name { position: absolute; left: 0; width: 781px; top: 268px; text-align: center; font-size: 104px; line-height: 1; letter-spacing: 2px; font-weight: 400; }
  .brand-tagline { position: absolute; left: 0; width: 781px; top: 385px; text-align: center; font-size: 58px; line-height: 1; font-weight: 400; }

  .metal-bar { position: absolute; left: 0; width: 781px; height: 19px;
    background: linear-gradient(90deg, var(--bar-edge), var(--bar-mid) 30%, var(--white) 55%, var(--bar-mid) 80%, var(--bar-edge)); }
  .bar-top { top: 467px; }
  .bar-middle { top: 994px; }
  .bar-bottom { top: 1166px; height: 34px; }

  .hero { position: absolute; left: 0; top: 486px; width: 781px; height: 508px;
    background: linear-gradient(160deg, #2a7fae, var(--sky) 50%, #2b7fb0); }

  .feature { position: absolute; display: flex; align-items: center; }
  .feature svg { flex: none; width: 74px; height: 74px; }
  .feature p { margin-left: 21px; font-size: 32px; line-height: 35px; }

  .contact { position: absolute; left: 71px; top: 1022px; font-size: 32px; line-height: 47px; }
</style>
</head>
<body>
<main class="flyer">
  <header class="masthead">
    <div class="mark-circle"></div>
    <h1 class="brand-name">HAWKIRON</h1>
    <p class="brand-tagline">STRUCTURAL</p>
  </header>

  <div class="metal-bar bar-top"></div>

  <section class="hero" role="img" aria-label="Upward view of a glass and steel office tower against a blue sky"></section>

  <svg width="0" height="0" style="position:absolute">
    <defs>
      <linearGradient id="tileFrame" x1="0" y1="0" x2="1" y2="1">
        <stop offset="0" stop-color="#2b4f97"/>
        <stop offset=".45" stop-color="#ffffff"/>
        <stop offset="1" stop-color="#3a5fae"/>
      </linearGradient>
    </defs>
  </svg>

  <div class="feature" style="left:68px; top:515px;">
    <svg viewBox="0 0 74 74"><rect x="2" y="2" width="70" height="70" rx="10" fill="url(#tileFrame)"/><rect x="8" y="8" width="58" height="58" rx="6" fill="var(--tile-fill)"/>
      <g stroke="var(--icon-ink)" stroke-width="2"><line x1="37" y1="18" x2="37" y2="56"/><line x1="18" y1="37" x2="56" y2="37"/><line x1="24" y1="24" x2="50" y2="50"/><line x1="50" y1="24" x2="24" y2="50"/></g>
      <rect x="32" y="8" width="10" height="8" fill="var(--icon-ink)"/></svg>
    <p>Laser Accuracy</p>
  </div>

  <div class="feature" style="left:68px; top:610px;">
    <svg viewBox="0 0 74 74"><rect x="2" y="2" width="70" height="70" rx="10" fill="url(#tileFrame)"/><rect x="8" y="8" width="58" height="58" rx="6" fill="var(--tile-fill)"/>
      <circle cx="37" cy="37" r="20" fill="none" stroke="var(--icon-ink)" stroke-width="3" stroke-dasharray="4 6"/>
      <g stroke="var(--icon-ink)" stroke-width="3"><line x1="37" y1="37" x2="37" y2="24"/><line x1="37" y1="37" x2="46" y2="37"/></g></svg>
    <p>On-time<br>scheduling</p>
  </div>

  <div class="feature" style="left:68px; top:702px;">
    <svg viewBox="0 0 74 74"><rect x="2" y="2" width="70" height="70" rx="10" fill="url(#tileFrame)"/><rect x="8" y="8" width="58" height="58" rx="6" fill="var(--tile-fill)"/>
      <circle cx="30" cy="44" r="11" fill="none" stroke="var(--icon-ink)" stroke-width="7" stroke-dasharray="4 3"/><circle cx="30" cy="44" r="5" fill="var(--icon-ink)"/>
      <circle cx="49" cy="25" r="7" fill="none" stroke="var(--icon-ink)" stroke-width="5" stroke-dasharray="3 2.5"/></svg>
    <p>Own our<br>Equipment</p>
  </div>

  <div class="feature" style="left:68px; top:794px;">
    <svg viewBox="0 0 74 74"><rect x="2" y="2" width="70" height="70" rx="10" fill="url(#tileFrame)"/><rect x="8" y="8" width="58" height="58" rx="6" fill="var(--tile-fill)"/>
      <circle cx="37" cy="37" r="21" fill="none" stroke="var(--icon-ink)" stroke-width="5" stroke-dasharray="3 4"/><circle cx="37" cy="37" r="11" fill="var(--icon-ink)"/></svg>
    <p>39 Years Exp.</p>
  </div>

  <div class="feature" style="left:68px; top:886px;">
    <svg viewBox="0 0 74 74"><rect x="2" y="2" width="70" height="70" rx="10" fill="url(#tileFrame)"/><rect x="8" y="8" width="58" height="58" rx="6" fill="var(--tile-fill)"/>
      <path d="M29 42 L24 62 L31 58 L35 64 L37 46 Z M45 42 L50 62 L43 58 L39 64 L37 46 Z" fill="var(--icon-ink)"/>
      <circle cx="37" cy="31" r="15" fill="var(--icon-ink)"/>
      <path d="M30 31 L35 36 L44 26" fill="none" stroke="var(--white)" stroke-width="3"/></svg>
    <p>Certified<br>welders</p>
  </div>

  <div class="feature" style="left:406px; top:517px; align-items:flex-start;">
    <svg viewBox="0 0 74 74"><rect x="2" y="2" width="70" height="70" rx="10" fill="url(#tileFrame)"/><rect x="8" y="8" width="58" height="58" rx="6" fill="var(--tile-fill)"/>
      <rect x="14" y="14" width="46" height="46" rx="6" fill="var(--icon-ink)"/>
      <g fill="var(--tile-fill)"><circle cx="23" cy="23" r="3"/><circle cx="51" cy="23" r="3"/><circle cx="23" cy="51" r="3"/><circle cx="51" cy="51" r="3"/><rect x="34" y="22" width="5" height="12" rx="2"/><rect x="34" y="40" width="5" height="12" rx="2"/></g></svg>
    <p style="margin-top:2px">Manufacturing<br>Construction<br>Brackets Since<br>1982</p>
  </div>

  <div class="feature" style="left:406px; top:713px; align-items:flex-start;">
    <svg viewBox="0 0 74 74"><rect x="2" y="2" width="70" height="70" rx="10" fill="url(#tileFrame)"/><rect x="8" y="8" width="58" height="58" rx="6" fill="var(--tile-fill)"/>
      <path d="M18 20 H56 V28 H42 V46 H56 V54 H18 V46 H32 V28 H18 Z" fill="var(--icon-ink)"/></svg>
    <p style="margin-top:2px">We manufacture<br>custom ibeams in<br>Phoenix, AZ</p>
  </div>

  <div class="metal-bar bar-middle"></div>

  <footer style="position:absolute; left:0; top:1013px; width:781px; height:153px; background:var(--address-blue);">
    <address class="contact" style="top:9px; font-style:normal;">
      Hawkiron Plant<br>
      4812 n. 27th street, suite-3 | Phx, AZ 85019<br>
      480-926-8147
    </address>
  </footer>

  <div class="metal-bar bar-bottom"></div>
</main>
</body>
</html>
```